Business Card and Logo tweak for a Language Boarding School

we are a boadring langauge school for under 18 international student.
We call ourselves " TWSC" - Tarravale Worldwide Studies Centre
We are one of the RV "rosewood venture" Melbourne campus for RV high school preparation program.

our address is 19 Tolley Road Ashcombe 3294
Ph: 03 84210563
Email: info@mytwsc.com
Website: www.mytwsc.com

We have our TWSC logo, but not very satisfied. May be you can tweak it furhter with the fond or formations.

Basically the business card list all relevant info on one side and list all our programs on the other side.

The program we have:
ELICOS with Boarding for U18 Students
HSP-High School Preparation Program
PSP- Primary School Preparation Program
Junior Holiday Program & Study Tours
After School Tutoring
Student Wellbeing and Counselling

```html
<!DOCTYPE html>
<html lang="en">
<head>
<meta charset="utf-8">
<title>TWSC Business Card</title>
<link rel="stylesheet" href="https://fonts.googleapis.com/css2?family=Jost:wght@400;600&family=Oswald:wght@300&display=swap">
<style>
  :root {
    --canvas-bg: #eeefee;
    --card-white: #ffffff;
    --brand-purple: #4d1289;
    --text-light: #ffffff;
  }
  * { margin: 0; padding: 0; box-sizing: border-box; }
  html, body {
    width: 1200px;
    height: 873px;
    overflow: hidden;
    background: var(--canvas-bg);
  }
  .canvas {
    position: relative;
    width: 1200px;
    height: 873px;
  }
  .card {
    position: absolute;
    top: 148px;
    width: 330px;
    height: 576px;
    border-radius: 22px;
  }
  .card--front {
    left: 242px;
    background: var(--card-white);
  }
  .card--back {
    left: 628px;
    background: var(--brand-purple);
    color: var(--text-light);
  }
  .brand-mark {
    position: absolute;
    left: 0;
    right: 0;
    top: 210px;
    display: flex;
    align-items: center;
    justify-content: center;
    gap: 12px;
  }
  .brand-mark__dot {
    width: 22px;
    height: 22px;
    border-radius: 50%;
    background: var(--brand-purple);
  }
  .brand-mark__name {
    font-family: "Jost", sans-serif;
    font-weight: 600;
    font-size: 46px;
    letter-spacing: 2px;
    color: var(--brand-purple);
  }
  .org-name {
    position: absolute;
    left: 38px;
    top: 48px;
    font-family: "Jost", sans-serif;
    font-weight: 600;
    font-size: 18px;
    line-height: 23px;
    letter-spacing: 0.5px;
    text-transform: uppercase;
  }
  .address {
    position: absolute;
    left: 38px;
    top: 181px;
    font-family: "Jost", sans-serif;
    font-weight: 400;
    font-size: 18px;
    line-height: 22px;
    letter-spacing: 0.5px;
  }
  .contact {
    position: absolute;
    left: 38px;
    top: 248px;
    font-family: "Jost", sans-serif;
    font-weight: 400;
    list-style: none;
  }
  .contact__item {
    display: flex;
    align-items: center;
    gap: 10px;
    font-size: 18px;
    line-height: 23px;
    letter-spacing: 0.5px;
  }
  .contact__item--web {
    font-size: 15px;
    line-height: 20px;
  }
  .contact__icon {
    width: 12px;
    height: 12px;
    flex: none;
  }
  .programs {
    position: absolute;
    left: 38px;
    top: 382px;
    list-style: none;
    font-family: "Oswald", sans-serif;
    font-weight: 300;
    font-size: 17px;
    line-height: 22px;
    letter-spacing: 0.2px;
  }
</style>
</head>
<body>
<main class="canvas">
  <section class="card card--front">
    <div class="brand-mark">
      <span class="brand-mark__dot"></span>
      <span class="brand-mark__name">TWSC</span>
    </div>
  </section>

  <section class="card card--back">
    <h1 class="org-name">Tarravale<br>Worldwide<br>Studies Centre</h1>

    <p class="address">19 Tolley Road<br>Ashcombe 3294</p>

    <ul class="contact">
      <li class="contact__item">
        <svg class="contact__icon" viewBox="0 0 12 12" aria-hidden="true">
          <path d="M2.5 1 L4.5 3.2 L3.4 4.6 C4.2 6.3 5.6 7.7 7.3 8.5 L8.7 7.4 L11 9.4 L9.8 11 C5.2 10.7 1.2 6.7 1 2.2 Z" fill="none" stroke="#fff" stroke-width="0.9" stroke-linejoin="round"/>
        </svg>
        <span>03 84210563</span>
      </li>
      <li class="contact__item">
        <svg class="contact__icon" viewBox="0 0 12 12" aria-hidden="true">
          <rect x="0.8" y="3" width="10.4" height="6.4" rx="0.8" fill="none" stroke="#fff" stroke-width="0.9"/>
          <path d="M1 3.4 L6 6.8 L11 3.4" fill="none" stroke="#fff" stroke-width="0.9"/>
        </svg>
        <span>info@mytwsc.com</span>
      </li>
      <li class="contact__item contact__item--web">www.mytwsc.com</li>
    </ul>

    <ul class="programs">
      <li>ELICOS with Boarding for U18 Students</li>
      <li>HSP-High School Preparation Program</li>
      <li>PSP-Primary School Preparation Program</li>
      <li>Junior Holiday Program &amp; Study Tours</li>
      <li>After School Tutoring</li>
      <li>Student Wellbeing and Counselling</li>
    </ul>
  </section>
</main>
</body>
</html>
```